Corporate Template

Looking for a set of corporate slides to be made which contain multiple different slides and orientations. Looking for at least 8 to 10 different master pages plus a Coversheet and closeout page. Incorporating a color palate similar to our logo coloring is preferred.
I have attached a logo.
I like the clever pixel yard designs best so far. They seem to fit what I'm looking for in terms of visual appearance.
Reason: I'm trying to allow time for a couple new designers to incorporate some changes I requested to their existing designs.

```html
<!DOCTYPE html>
<html lang="en">
<head>
<meta charset="utf-8">
<title>Halcyon Neurometrics – Cover Slide</title>
<link rel="stylesheet" href="https://fonts.googleapis.com/css2?family=Titillium+Web:wght@400;600&display=swap">
<style>
  :root {
    --brand-blue: #2f6daf;
    --brand-blue-deep: #2a62a0;
    --brand-blue-light: #8cbcec;
    --text-dark: #1d1d1d;
    --divider: #e6e6e6;
    --paper: #ffffff;
  }
  * { margin: 0; padding: 0; box-sizing: border-box; }
  html, body { width: 1200px; height: 900px; overflow: hidden; background: var(--paper); }
  body { font-family: "Titillium Web", sans-serif; }

  .slide { position: relative; width: 1200px; height: 900px; overflow: hidden; background: var(--paper); }

  .brand-mark {
    position: absolute; top: 300px; left: 0; width: 1200px;
    text-align: center; color: var(--brand-blue); font-weight: 600; line-height: 1;
  }
  .brand-mark__name { font-size: 74px; letter-spacing: 1px; }
  .brand-mark__line { font-size: 31px; letter-spacing: 1px; margin-top: 14px; }

  .divider {
    position: absolute; left: 383px; width: 480px; height: 2px;
    background: linear-gradient(90deg, transparent, var(--divider) 20%, var(--divider) 80%, transparent);
  }
  .divider--top { top: 479px; }
  .divider--bottom { top: 585px; }

  .presenter { position: absolute; top: 492px; left: 0; width: 1200px; text-align: center; }
  .presenter__name { font-size: 36px; font-weight: 400; color: var(--brand-blue); line-height: 1.1; }
  .presenter__role { font-size: 27px; font-weight: 600; color: var(--text-dark); line-height: 1.4; }

  .project-title {
    position: absolute; top: 622px; left: 0; width: 1200px; text-align: center;
    font-size: 58px; font-weight: 400; color: var(--brand-blue); line-height: 1.2;
  }

  .footer-band { position: absolute; left: 0; top: 0; width: 1200px; height: 900px; }

  .footer-brand {
    position: absolute; left: 30px; top: 806px; color: var(--paper);
    font-weight: 400; line-height: 1;
  }
  .footer-brand__name { font-size: 42px; }
  .footer-brand__line { font-size: 18px; margin-top: 4px; letter-spacing: 0.5px; }

  .copyright {
    position: absolute; left: 786px; top: 862px; font-size: 20px;
    color: var(--brand-blue-light); line-height: 1;
  }
  .page-number {
    position: absolute; left: 1145px; top: 833px; width: 38px; height: 38px; border-radius: 50%;
    background: var(--paper); color: var(--brand-blue-deep);
    font-size: 17px; font-weight: 600; display: flex; align-items: center; justify-content: center;
  }
</style>
</head>
<body>
<main class="slide">
  <div class="brand-mark">
    <div class="brand-mark__name">HALCYON</div>
    <div class="brand-mark__line">NEUROMETRICS</div>
  </div>

  <div class="divider divider--top"></div>
  <div class="presenter">
    <p class="presenter__name">Company Founder</p>
    <p class="presenter__role">Co-founder</p>
  </div>
  <div class="divider divider--bottom"></div>

  <h1 class="project-title">Project Title here</h1>

  <svg class="footer-band" viewBox="0 0 1200 900" aria-hidden="true">
    <defs>
      <linearGradient id="bandFill" x1="0" y1="0" x2="1" y2="0">
        <stop offset="0" stop-color="#2c66a6"/>
        <stop offset="1" stop-color="#3a7cc0"/>
      </linearGradient>
    </defs>
    <path d="M0,737 C300,800 520,848 720,842 C950,834 1100,765 1200,722 L1200,900 L0,900 Z" fill="url(#bandFill)"/>
    <path d="M0,737 C300,800 520,848 720,842 C950,834 1100,765 1200,722" fill="none" stroke="#8cbcec" stroke-width="4"/>
    <line x1="0" y1="858" x2="1200" y2="858" stroke="#5a93cf" stroke-width="1.5" opacity="0.6"/>
  </svg>

  <div class="footer-brand">
    <div class="footer-brand__name">HALCYON</div>
    <div class="footer-brand__line">NEUROMETRICS</div>
  </div>

  <p class="copyright">Copyright text here</p>
  <div class="page-number">01</div>
</main>
</body>
</html>
```